Vantelle Naturals- An All Natural Hair & Skincare Company needs a website design.

Vantelle Naturals is an all-natural Hair & Skin Company that provides all natural hair and skin care products to the ever growing natural hair community. Our primary target market is African American women between the ages of 16-50. I would like my website to be setup in a way that allows me to add photos, and products for sale easily. The site should be very user friendly but clean and professional looking. I have uploaded our new company Logo and I would definitely like it used throughout the pages. Ideally, the site should display our Motto, Company Vision, Pictures of Products and Results of use of products, testimonials from customers, Video tutorials. I need to be able to capture email addresses for easy email blasts and customer data collection, contact info, links to social media accounts, and detailed analytics to track traffic etc. I also need direct links to my PayPal and email.

It appears my brief is unclear. This is our first site. So i would like it to be able to showcase and all my products. I would like the coding for easy changes after the site goes live. I am not super tech savvy, but would like to be able to add new products and track traffic. Please let me know if this still needs clarification.

Industry/Entity Type

Hair

Coding

Coded - Design and coding required

```html
<!DOCTYPE html>
<html lang="en">
<head>
<meta charset="utf-8">
<title>Vantelle Naturals – All Natural Hair &amp; Skincare</title>
<link rel="stylesheet" href="https://fonts.googleapis.com/css2?family=Lato:wght@400;700&family=Arimo:wght@700&display=swap">
<style>
  :root {
    --brown: #a8774f;
    --brown-text: #a27a57;
    --brown-dark: #8a5f3e;
    --slate: #434c4a;
    --white: #ffffff;
    --rule: #9a9a9a;
    --green-light: #d4f21a;
    --green-mid: #8fbf2a;
    --green-deep: #5d8f22;
  }
  * { margin: 0; padding: 0; box-sizing: border-box; }
  html, body {
    width: 1200px; height: 560px; overflow: hidden;
    background: var(--white);
    font-family: "Lato", sans-serif;
  }
  .page { position: relative; width: 1200px; height: 560px; }

  .site-header {
    position: absolute; top: 0; left: 0; width: 1200px; height: 66px;
    background: var(--white);
    border-bottom: 3px solid var(--brown);
    height: 69px;
  }
  .brand {
    position: absolute; left: 302px; top: 18px;
    display: flex; align-items: center; gap: 10px;
    color: var(--brown-text); font-size: 19px; font-weight: 400;
    text-decoration: none;
  }
  .brand-dot { width: 30px; height: 30px; border-radius: 50%; background: var(--brown-dark); }
  .main-nav { position: absolute; top: 31px; left: 533px; display: flex; gap: 44px; }
  .main-nav a {
    color: var(--brown-text); font-size: 13px; text-decoration: none;
  }

  .hero {
    position: absolute; top: 69px; left: 0; width: 1200px; height: 251px;
    background: var(--slate);
  }
  .hero-image {
    position: absolute; left: 298px; top: 0; width: 604px; height: 251px;
    background:
      radial-gradient(circle at 45% 85%, var(--green-light) 0%, rgba(212,242,26,0) 35%),
      radial-gradient(circle at 85% 25%, #dfeede 0%, rgba(223,238,222,0) 30%),
      linear-gradient(120deg, var(--green-deep) 0%, var(--green-mid) 45%, #b7dc4a 75%, #cfe6c4 100%);
  }

  .motto-band {
    position: absolute; top: 320px; left: 0; width: 1200px; height: 98px;
    background: var(--brown);
  }
  .motto {
    position: absolute; left: 311px; top: 13px; color: var(--white);
  }
  .motto-line { font-size: 18px; line-height: 24px; }
  .motto-sign {
    margin-top: 5px; font-family: "Arimo", sans-serif; font-weight: 700; font-size: 13px;
  }
  .motto-mark {
    position: absolute; left: 776px; top: 16px; width: 60px; height: 60px;
    border-radius: 50%; background: var(--brown-dark);
  }

  .products {
    position: absolute; top: 438px; left: 298px; width: 604px;
  }
  .section-title {
    color: var(--brown-text); font-size: 20px; font-weight: 400;
    padding-bottom: 8px; border-bottom: 1px solid var(--rule);
  }
  .product-row { position: relative; height: 100px; }
  .product-shot { position: absolute; top: 18px; height: 90px; }
  .product-shot.green { left: 20px; width: 152px; background: linear-gradient(90deg, #b9d24a, #cfe07a 60%, #a6c23a); }
  .product-shot.mixed { left: 210px; width: 187px; background: linear-gradient(90deg, #a9c44e, #d76b3a 45%, #e6e6e6 65%, #3aa9d8); }
  .product-shot.silver { left: 414px; width: 183px; background: linear-gradient(90deg, #d8d8d8, #f2f2f2 50%, #c4c4c4); }
</style>
</head>
<body>
<div class="page">
  <header class="site-header">
    <a class="brand" href="#"><span class="brand-dot"></span>Vantelle Naturals</a>
    <nav class="main-nav">
      <a href="#">Home</a>
      <a href="#">Products</a>
      <a href="#">About Us</a>
      <a href="#">Contact</a>
    </nav>
  </header>

  <section class="hero">
    <div class="hero-image" role="img" aria-label="Soft-focus green foliage background"></div>
  </section>

  <section class="motto-band">
    <div class="motto">
      <p class="motto-line">Healthy Hair and Skin is our Priority...</p>
      <p class="motto-line">A Beautiful YOU is OUR specialty!!</p>
      <p class="motto-sign">- Vantelle Naturals</p>
    </div>
    <div class="motto-mark"></div>
  </section>

  <section class="products">
    <h2 class="section-title">Try our products</h2>
    <div class="product-row">
      <div class="product-shot green" role="img" aria-label="Green skincare bottles and boxes"></div>
      <div class="product-shot mixed" role="img" aria-label="Row of colourful hair care bottles"></div>
      <div class="product-shot silver" role="img" aria-label="Silver and white cosmetic pump bottles and jars"></div>
    </div>
  </section>
</div>
</body>
</html>
```